Graphic Design of Business Process

We require an eye-catching, sophisticated design of 2 business processes (attached), that will be used digitally AND for print (to be put on walls in our office).

The basic layout is attached. We require a creative, professional designer to re-design these so that they look appealing but still able to grasp all the information.

We will require vector files and editable project files for final delivery. You may refer to our website (lanternwickhub.com.au) for an indication of our brand.

If you have any questions, please ask.

Thank you.

```html
<!DOCTYPE html>
<html lang="en">
<head>
<meta charset="utf-8">
<title>Content Hierarchy</title>
<link href="https://fonts.googleapis.com/css2?family=Montserrat:wght@800;900&family=Oswald:wght@700&display=swap" rel="stylesheet">
<style>
  :root {
    --ink: #0d0d0d;
    --accent-bar: #f7b439;
    --bg-centre: #ffffff;
    --bg-edge: #9dd6f4;
    --panel: #ffffff;
    --panel-edge: #e3e5e8;
    --hero: #4a5aa8;
    --hero-deep: #3b4581;
    --hero-text: #4752a0;
    --hub: #b8499f;
    --hub-deep: #8c3a7c;
    --hub-text: #b0449a;
    --hygiene: #f8a62a;
    --hygiene-deep: #b7853f;
    --hygiene-text: #f39a1c;
    --inner-shade: #d4d6d9;
  }
  html, body {
    margin: 0;
    padding: 0;
    width: 1200px;
    height: 2311px;
    overflow: hidden;
  }
  .poster {
    display: block;
    width: 1200px;
    height: 2311px;
  }
  .title {
    font-family: "Montserrat", sans-serif;
    font-weight: 900;
    font-size: 76px;
    fill: var(--ink);
    text-anchor: middle;
  }
  .tier-name, .tier-desc {
    font-family: "Oswald", sans-serif;
    font-weight: 700;
    text-anchor: middle;
  }
  .tier-name { font-size: 46px; }
  .tier-desc { font-size: 40px; }
  .brand-name {
    font-family: "Montserrat", sans-serif;
    font-weight: 800;
    font-size: 24px;
    letter-spacing: 5px;
    fill: var(--ink);
    text-anchor: middle;
  }
  .panel { fill: var(--panel); stroke: var(--panel-edge); stroke-width: 4; }
  .hex-inner { fill: #ffffff; }
  .hex-shade { fill: var(--inner-shade); }
  .tier-hero .hex-outer, .tier-hero .panel-bar { fill: var(--hero); }
  .tier-hero .hex-band { fill: var(--hero-deep); }
  .tier-hero text { fill: var(--hero-text); }
  .tier-hub .hex-outer, .tier-hub .panel-bar { fill: var(--hub); }
  .tier-hub .hex-band { fill: var(--hub-deep); }
  .tier-hub text { fill: var(--hub-text); }
  .tier-hygiene .hex-outer, .tier-hygiene .panel-bar { fill: var(--hygiene); }
  .tier-hygiene .hex-band { fill: var(--hygiene-deep); }
  .tier-hygiene text { fill: var(--hygiene-text); }
</style>
</head>
<body>
<svg class="poster" viewBox="0 0 780 1502" preserveAspectRatio="none" xmlns="http://www.w3.org/2000/svg">
  <defs>
    <radialGradient id="bg-glow" cx="50%" cy="55%" r="75%">
      <stop offset="0%" stop-color="var(--bg-centre)"/>
      <stop offset="55%" stop-color="#eaf6fd"/>
      <stop offset="100%" stop-color="var(--bg-edge)"/>
    </radialGradient>
    <polygon id="hex" points="0,-160 130,-80 130,80 0,160 -130,80 -130,-80"/>
  </defs>

  <rect class="backdrop" width="780" height="1502" fill="url(#bg-glow)"/>

  <text class="title" x="390" y="132">CONTENT</text>
  <text class="title" x="390" y="236" textLength="484" lengthAdjust="spacingAndGlyphs">HIERARCHY</text>
  <rect class="title-rule" x="148" y="258" width="484" height="12" fill="var(--accent-bar)"/>

  <g class="tier tier-hero" transform="translate(0,468)">
    <rect class="panel" x="292" y="-132" width="366" height="262"/>
    <rect class="panel-bar" x="636" y="-126" width="16" height="250"/>
    <g transform="translate(255,0)">
      <use href="#hex" class="hex-outer"/>
      <use href="#hex" class="hex-band" transform="scale(0.88)"/>
      <use href="#hex" class="hex-shade" transform="scale(0.78)"/>
      <use href="#hex" class="hex-inner" transform="translate(3,4) scale(0.76)"/>
      <text class="tier-name" x="0" y="16">HERO</text>
    </g>
    <text class="tier-desc" x="503" y="-18">TENTPOLE</text>
    <text class="tier-desc" x="503" y="46">CAMPAIGNS</text>
  </g>

  <g class="tier tier-hub" transform="translate(0,828)">
    <rect class="panel" x="292" y="-134" width="366" height="260"/>
    <rect class="panel-bar" x="636" y="-128" width="16" height="248"/>
    <g transform="translate(255,0)">
      <use href="#hex" class="hex-outer"/>
      <use href="#hex" class="hex-band" transform="scale(0.88)"/>
      <use href="#hex" class="hex-shade" transform="scale(0.78)"/>
      <use href="#hex" class="hex-inner" transform="translate(3,4) scale(0.76)"/>
      <text class="tier-name" x="0" y="16">HUB</text>
    </g>
    <text class="tier-desc" x="498" y="-50">REGULAR</text>
    <text class="tier-desc" x="498" y="12">“PUSH”</text>
    <text class="tier-desc" x="498" y="74">CONTENT</text>
  </g>

  <g class="tier tier-hygiene" transform="translate(0,1195)">
    <rect class="panel" x="292" y="-130" width="366" height="260"/>
    <rect class="panel-bar" x="636" y="-124" width="16" height="248"/>
    <g transform="translate(255,0)">
      <use href="#hex" class="hex-outer"/>
      <use href="#hex" class="hex-band" transform="scale(0.88)"/>
      <use href="#hex" class="hex-shade" transform="scale(0.78)"/>
      <use href="#hex" class="hex-inner" transform="translate(3,4) scale(0.76)"/>
      <text class="tier-name" x="0" y="16">HYGIENE</text>
    </g>
    <text class="tier-desc" x="512" y="-52">ALWAYS-ON</text>
    <text class="tier-desc" x="512" y="12">“PULL”</text>
    <text class="tier-desc" x="512" y="76">CONTENT</text>
  </g>

  <text class="brand-name" x="390" y="1440">LANTERNWICK HUB</text>
</svg>
</body>
</html>
```